Loom Haven needs a website

I sell rugs and carpet on my website, loomhavenfloors.example. I need help with the site design to make it "pop". The logo in the header has been designed and I want the site to match it's style and color. Also I have some example sites for layout:
matvale.example
weave-outlet.example

Industry/Entity Type

Carpet

Requirements
Must have
• Scrolling images on front page. I will insert photos, just need the code.

```html
<!DOCTYPE html>
<html lang="en">
<head>
<meta charset="utf-8">
<title>Loom Haven – Carpet &amp; Rugs</title>
<link href="https://fonts.googleapis.com/css2?family=Open+Sans:wght@400;600;700&display=swap" rel="stylesheet">
<style>
:root{
  --green:#5bb73b;
  --green-dark:#4a9a2f;
  --ink:#2e2e2e;
  --dark:#333537;
  --darker:#26282a;
  --grey-bg:#e9e9e9;
  --line:#dcdcdc;
  --muted:#8a8a8a;
  --red:#c9302c;
  --white:#ffffff;
}
*{box-sizing:border-box;margin:0;padding:0}
html,body{width:713px;height:1200px;overflow:hidden}
body{background:var(--grey-bg);font-family:"Open Sans",Arial,sans-serif;color:var(--ink);font-size:8px}
.page{position:relative;width:520px;height:1200px;margin:0 auto;background:var(--white)}
/* header */
.site-header{position:relative;height:102px;background:var(--white)}
.brand{position:absolute;left:10px;top:16px;display:flex;align-items:center;gap:6px}
.brand-mark{width:14px;height:14px;border-radius:50%;background:var(--green)}
.brand-name{font-size:19px;font-weight:700;color:var(--ink);letter-spacing:-.3px}
.header-bar{position:absolute;right:0;top:0;width:345px;height:102px;background:var(--dark)}
.utility{display:flex;justify-content:flex-end;align-items:center;gap:12px;height:52px;padding-right:10px;color:#ddd;font-size:7.5px}
.utility .flag{width:14px;height:9px;background:linear-gradient(#c33 0 33%,#fff 33% 66%,#2a4d9b 66%)}
.cart-btn{background:var(--green);color:var(--white);padding:5px 9px;font-weight:600;border-radius:2px}
.main-nav{display:flex;align-items:center;height:50px;border-top:1px solid #444;padding-left:8px}
.main-nav a{color:var(--white);text-decoration:none;font-size:8px;font-weight:600;padding:0 9px}
.search-btn{margin-left:auto;width:50px;height:50px;background:var(--green);display:flex;align-items:center;justify-content:center}
/* hero */
.hero{position:relative;height:230px;margin:4px 0 0}
.hero-photo{position:absolute;inset:0;background:linear-gradient(100deg,#d9d3c8 0%,#b58a5a 30%,#8e3f2f 55%,#6b7d3c 75%,#c66b2a 100%)}
.hero-caption{position:absolute;left:14px;top:120px;color:var(--white)}
.hero-caption h1{font-size:17px;font-weight:700;margin-bottom:4px}
.hero-caption p{font-size:7px;width:170px;line-height:1.4;margin-bottom:8px}
.btn{display:inline-block;background:var(--green);color:var(--white);font-weight:600;font-size:8px;padding:6px 12px;border-radius:2px}
.hero-dots{position:absolute;left:14px;bottom:14px;display:flex;gap:4px}
.hero-dots span{width:6px;height:6px;border-radius:50%;background:rgba(255,255,255,.6)}
.hero-dots span:first-child{background:var(--white)}
/* categories */
.category-tiles{display:flex;gap:12px;margin-top:10px;height:92px}
.tile{position:relative;flex:1}
.tile-photo{position:absolute;inset:0}
.tile-label{position:absolute;left:0;bottom:0;right:0;padding:5px 6px;background:rgba(0,0,0,.55);color:var(--white);font-weight:700;font-size:9px}
/* main */
.main{display:flex;gap:12px;margin-top:12px;height:378px}
.sidebar{width:125px}
.panel-head{background:var(--green);color:var(--white);font-weight:700;font-size:8.5px;padding:7px 8px}
.cat-list{list-style:none;border:1px solid var(--line);border-top:0;margin-bottom:10px}
.cat-list li{padding:6px 8px;border-top:1px solid var(--line);font-size:7px;color:#555}
.cat-list li::before{content:"› ";color:var(--green)}
.login-box{background:var(--green-dark);padding:8px;margin-bottom:10px}
.login-box .field{height:14px;background:var(--white);border-radius:2px;margin-bottom:5px}
.login-row{display:flex;justify-content:space-between;align-items:center;color:var(--white);font-size:6.5px}
.login-row .btn-red{background:var(--red);color:var(--white);padding:3px 8px;font-weight:600;border-radius:2px}
.specials-head{background:var(--green);color:var(--white);font-weight:700;font-size:10px;padding:6px 8px;text-align:center}
.specials{border:1px solid var(--line);border-top:0;padding:8px;text-align:center}
.specials .pic{height:66px;margin-bottom:6px}
.specials .name{font-size:7px;font-weight:600;margin-bottom:3px}
.old{color:var(--muted);text-decoration:line-through;font-size:8px;margin-right:4px}
.now{color:var(--red);font-weight:700;font-size:9px}
.featured{flex:1}
.featured-head{display:flex;justify-content:space-between;align-items:center;border-bottom:2px solid var(--green);padding-bottom:5px;margin-bottom:10px}
.featured-head h2{font-size:10px;font-weight:700}
.arrows{display:flex;gap:3px}
.arrows span{width:13px;height:13px;background:var(--green);color:var(--white);font-size:8px;display:flex;align-items:center;justify-content:center}
.grid{display:grid;grid-template-columns:repeat(4,1fr);gap:12px 10px}
.card{border:1px solid var(--line)}
.card .pic{height:72px}
.card .info{padding:5px}
.card .title{font-size:7px;font-weight:600;margin-bottom:2px}
.card .meta{font-size:5.5px;color:var(--muted);line-height:1.4;margin-bottom:5px}
.card .buy{display:flex;justify-content:space-between;align-items:center}
.price{color:var(--green);font-weight:700;font-size:9px}
.cart-icon{width:16px;height:14px;background:var(--green);display:flex;align-items:center;justify-content:center}
/* features */
.features{display:flex;justify-content:space-around;background:var(--dark);height:70px;margin-top:12px;align-items:center}
.feature{display:flex;align-items:center;gap:7px;color:var(--white)}
.feature b{display:block;font-size:10px}
.feature small{font-size:6px;color:#bbb}
/* footer */
.site-footer{background:var(--darker);margin-top:10px;height:200px;padding:16px 12px;display:flex;gap:16px;color:#aaa}
.footer-brand{width:130px}
.footer-brand .brand-name{color:#ccc;font-size:15px}
.footer-brand p{font-size:6.5px;line-height:1.9;margin-top:10px}
.social{display:flex;gap:4px;margin-top:8px}
.social span{width:11px;height:11px;border-radius:50%;background:#555}
.footer-col{flex:1}
.footer-col h3{color:var(--white);font-size:7.5px;font-weight:700;margin-bottom:8px;text-transform:uppercase}
.footer-col li{list-style:none;font-size:6.5px;line-height:1.9}
.newsletter{display:flex;align-items:center;gap:8px;background:var(--darker);border-top:1px solid #3a3a3a;height:30px;padding:0 12px;color:#ccc;font-size:6.5px}
.newsletter .input{width:120px;height:12px;background:#fff}
.newsletter .go{background:var(--green);color:#fff;padding:2px 6px;font-weight:600}
.pay{margin-left:auto;display:flex;gap:4px;align-items:center}
.pay span{width:20px;height:12px;background:#888;border-radius:2px}
.copyright{display:flex;justify-content:space-between;background:#1d1f20;color:#777;font-size:6px;padding:8px 12px}
</style>
</head>
<body>
<div class="page">
  <header class="site-header">
    <div class="brand"><span class="brand-mark"></span><span class="brand-name">Loom Haven</span></div>
    <div class="header-bar">
      <div class="utility">
        <span class="flag"></span><span>Login</span><span>Register</span>
        <span class="cart-btn">Cart · $0.00</span>
      </div>
      <nav class="main-nav">
        <a>Home</a><a>About Us</a><a>My Account</a><a>Our Products</a><a>Checkout</a>
        <span class="search-btn"><svg width="14" height="14" viewBox="0 0 14 14"><circle cx="6" cy="6" r="4.2" fill="none" stroke="#fff" stroke-width="1.6"/><line x1="9" y1="9" x2="13" y2="13" stroke="#fff" stroke-width="1.8"/></svg></span>
      </nav>
    </div>
  </header>

  <section class="hero">
    <div class="hero-photo" role="img" aria-label="Fan of carpet samples in many colours"></div>
    <div class="hero-caption">
      <h1>Carpet Flooring</h1>
      <p>Soft, durable carpet for every room, cut to size and shipped straight to your door.</p>
      <span class="btn">Shop Now</span>
    </div>
    <div class="hero-dots"><span></span><span></span><span></span><span></span></div>
  </section>

  <section class="category-tiles">
    <div class="tile"><div class="tile-photo" role="img" aria-label="Commercial office with carpet flooring" style="background:linear-gradient(#cfd4d6,#8c8f8a)"></div><div class="tile-label">Commercial Flooring</div></div>
    <div class="tile"><div class="tile-photo" role="img" aria-label="Living room with hardwood floor" style="background:linear-gradient(#d8c7aa,#8a5a33)"></div><div class="tile-label">Hardwood Flooring</div></div>
    <div class="tile"><div class="tile-photo" role="img" aria-label="Room with a patterned area rug" style="background:linear-gradient(#e0c8a8,#9b3b2c)"></div><div class="tile-label">Area Rugs</div></div>
  </section>

  <div class="main">
    <aside class="sidebar">
      <div class="panel-head">Shop by Category</div>
      <ul class="cat-list">
        <li>Commercial Flooring</li><li>Carpet Flooring</li><li>Hardwood Flooring</li><li>Area Rugs</li>
      </ul>
      <div class="login-box">
        <div class="field"></div><div class="field"></div>
        <div class="login-row"><span>Forgot login?</span><span class="btn-red">Login</span></div>
      </div>
      <div class="specials-head">Specials</div>
      <div class="specials">
        <div class="pic" role="img" aria-label="Rolls of commercial carpet" style="background:linear-gradient(135deg,#c77ba4,#7aa6c9)"></div>
        <div class="name">Commercial Carpet Roll</div>
        <span class="old">$59.99</span><span class="now">$55.86</span>
      </div>
    </aside>

    <section class="featured">
      <div class="featured-head"><h2>Featured Products</h2><div class="arrows"><span>‹</span><span>›</span></div></div>
      <div class="grid">
        <div class="card"><div class="pic" role="img" aria-label="Hickory hardwood planks" style="background:#c9a46b"></div><div class="info"><div class="title">American Hickory</div><div class="meta">Maker: Hardwood<br>Item No: HW-0110</div><div class="buy"><span class="price">$56.00</span><span class="cart-icon"><svg width="9" height="8" viewBox="0 0 9 8"><path d="M0 1h2l1 4h5l1-3H3" fill="none" stroke="#fff"/></svg></span></div></div></div>
        <div class="card"><div class="pic" role="img" aria-label="Beige area rug" style="background:#d8cfbc"></div><div class="info"><div class="title">Heirloom Weave</div><div class="meta">Maker: Area Rug<br>Item No: AR-0214</div><div class="buy"><span class="price">$56.00</span><span class="cart-icon"><svg width="9" height="8" viewBox="0 0 9 8"><path d="M0 1h2l1 4h5l1-3H3" fill="none" stroke="#fff"/></svg></span></div></div></div>
        <div class="card"><div class="pic" role="img" aria-label="Red carpet roll" style="background:#b2403a"></div><div class="info"><div class="title">Carpet Roll</div><div class="meta">Maker: Commercial<br>Item No: CR-0302</div><div class="buy"><span class="price">$56.00</span><span class="cart-icon"><svg width="9" height="8" viewBox="0 0 9 8"><path d="M0 1h2l1 4h5l1-3H3" fill="none" stroke="#fff"/></svg></span></div></div></div>
        <div class="card"><div class="pic" role="img" aria-label="Oak hardwood floor" style="background:#b88a55"></div><div class="info"><div class="title">Oak Plank</div><div class="meta">Maker: Hardwood<br>Item No: HW-0418</div><div class="buy"><span class="price">$56.00</span><span class="cart-icon"><svg width="9" height="8" viewBox="0 0 9 8"><path d="M0 1h2l1 4h5l1-3H3" fill="none" stroke="#fff"/></svg></span></div></div></div>
        <div class="card"><div class="pic" role="img" aria-label="Grey carpet sample" style="background:#a7a49c"></div><div class="info"><div class="title">Carpet Flooring</div><div class="meta">Maker: Carpet<br>Item No: CF-0520</div><div class="buy"><span class="price">$56.00</span><span class="cart-icon"><svg width="9" height="8" viewBox="0 0 9 8"><path d="M0 1h2l1 4h5l1-3H3" fill="none" stroke="#fff"/></svg></span></div></div></div>
        <div class="card"><div class="pic" role="img" aria-label="Deep red patterned rug" style="background:#9e2a3a"></div><div class="info"><div class="title">Style</div><div class="meta">Maker: Area Rug<br>Item No: AR-0631</div><div class="buy"><span class="price">$56.00</span><span class="cart-icon"><svg width="9" height="8" viewBox="0 0 9 8"><path d="M0 1h2l1 4h5l1-3H3" fill="none" stroke="#fff"/></svg></span></div></div></div>
        <div class="card"><div class="pic" role="img" aria-label="Dark red commercial carpet" style="background:#7e2a2e"></div><div class="info"><div class="title">Commercial Carpet</div><div class="meta">Maker: Commercial<br>Item No: CC-0744</div><div class="buy"><span class="price">$56.00</span><span class="cart-icon"><svg width="9" height="8" viewBox="0 0 9 8"><path d="M0 1h2l1 4h5l1-3H3" fill="none" stroke="#fff"/></svg></span></div></div></div>
        <div class="card"><div class="pic" role="img" aria-label="Green and grey carpet tiles" style="background:linear-gradient(135deg,#7d9a5a,#8e9497)"></div><div class="info"><div class="title">Carpet Tile</div><div class="meta">Maker: Commercial<br>Item No: CT-0856</div><div class="buy"><span class="price">$56.00</span><span class="cart-icon"><svg width="9" height="8" viewBox="0 0 9 8"><path d="M0 1h2l1 4h5l1-3H3" fill="none" stroke="#fff"/></svg></span></div></div></div>
      </div>
    </section>
  </div>

  <section class="features">
    <div class="feature"><svg width="26" height="18" viewBox="0 0 26 18"><rect x="0" y="2" width="16" height="11" fill="#fff"/><path d="M16 6h6l4 4v3h-10z" fill="#fff"/><circle cx="5" cy="15" r="2.5" fill="#fff"/><circle cx="20" cy="15" r="2.5" fill="#fff"/></svg><div><b>FREE SHIPPING</b><small>ON ORDERS OVER $99</small></div></div>
    <div class="feature"><svg width="20" height="20" viewBox="0 0 20 20"><rect x="1" y="7" width="18" height="12" fill="#fff"/><rect x="0" y="4" width="20" height="4" fill="#fff"/><rect x="9" y="4" width="2" height="15" fill="#333537"/></svg><div><b>SPECIAL GIFT CARDS</b><small>GIVE THE PERFECT GIFT</small></div></div>
    <div class="feature"><svg width="22" height="18" viewBox="0 0 22 18"><path d="M0 1h4l3 11h12l3-8H6" fill="none" stroke="#fff" stroke-width="2"/><circle cx="8" cy="16" r="2" fill="#fff"/><circle cx="18" cy="16" r="2" fill="#fff"/></svg><div><b>ORDER ONLINE</b><small>HOURS: 9AM–6PM EST</small></div></div>
  </section>

  <footer>
    <div class="site-footer">
      <div class="footer-brand">
        <span class="brand-name">Loom Haven</span>
        <p>48 Weaver Lane, Tuftford<br>hello@loomhavenfloors.example<br>Phone: (555) 014-2277</p>
        <div class="social"><span></span><span></span><span></span></div>
      </div>
      <div class="footer-col"><h3>Information</h3><ul><li>Commercial Flooring</li><li>Carpet Flooring</li><li>Hardwood Flooring</li><li>Area Rugs</li><li>Accessories</li><li>Wallpaper</li><li>Vinyl</li></ul></div>
      <div class="footer-col"><h3>Customer Support</h3><ul><li>About Us</li><li>Our Policies</li><li>Store Information</li><li>Shipping &amp; Care</li><li>Terms Of Use</li></ul></div>
      <div class="footer-col"><h3>My Account</h3><ul><li>Login</li><li>My Account</li><li>Contact Us</li><li>Order Status</li><li>Return Orders</li></ul></div>
    </div>
    <div class="newsletter"><span>NEWSLETTER SIGN UP</span><span class="input"></span><span class="go">SUBSCRIBE</span><div class="pay"><span>PAYMENTS:</span><span></span><span></span><span></span><span></span><span></span></div></div>
    <div class="copyright"><span>© 2024 Loom Haven. All Rights Reserved.</span><span>Terms of Service | Privacy Policy</span></div>
  </footer>
</div>
</body>
</html>
```